Brookvale Homes Flyer

Quarter-page leave-behind flyer for a commercial cleaning company (print)

ABOUT US
Quillon Commercial Cleaning is a Texas-owned commercial cleaning company serving Austin for over 20 years. We were recently named to Brookvale Homes's Capital Partner Roster Circle, a preferred vendor program covering apartment communities across the Austin metro. Our sales team will hand this flyer to apartment community managers during property visits.

THE JOB THIS FLYER MUST DO
A busy property manager should scan it in five seconds, understand what we do, trust us and keep the card on their desk. The call to action is booking a free walkthrough of their community. Do not include any pricing.

SPECS
Size: 4.25 x 5.5 inches (quarter of a letter page), single sided, portrait. Print ready with 0.125 inch bleed, CMYK, 300 dpi minimum. Vector preferred.

REQUIRED CONTENT
Headline: The clean your residents notice.
Badge or tagline: Brookvale Homes's Approved Austin Cleaning Company.
Supporting line: Preferred Vendor Partner in BVH's Capital Partner Roster Circle. Texas-owned, serving Austin for 20+ years.
Services (icons welcome): recurring janitorial, floor strip wax and buff, carpet extraction, windows and glass, upholstery care, pressure washing, move-in and move-out cleans, damage restoration.
Trust points: licensed and insured, background-checked crews, TrudeLink compliant, invoicing through Supplier Nook and Halvex Systems.

Social proof line: Already trusted by BVH communities. Ask your peers at The Wendlow and The Fennick on Garrow.

Call to action: Book a free walkthrough of your community. Call or email 512-555-0147 or support@quillonclean-example.com

STYLE DIRECTION
Clean, crisp and premium. Whiteness and shine should feel like part of the message. We like a deep green and teal palette with one warm accent, but strong alternative directions are welcome. Custom icons over clip art.
AVOID
Stock photos of cleaners with buckets, cartoon mascots, sparkle overload, cluttered layouts, any prices or dollar amounts.
DELIVERABLES
Print-ready PDF with bleed and crop marks, plus editable source files (AI, PSD or Figma). A version with our logo placement marked, since we will supply the logo file to the winner.

```html
<!DOCTYPE html>
<html lang="en">
<head>
<meta charset="utf-8">
<title>Brookvale Homes Flyer – Quillon Commercial Cleaning</title>
<link href="https://fonts.googleapis.com/css2?family=Figtree:wght@300;400;500;600;700;800&family=Playfair+Display:wght@400;700&display=swap" rel="stylesheet">
<style>
:root{
  --green-deep:#0d3a35;
  --teal-band:#064a44;
  --gold:#c99a52;
  --gold-text:#d4a35c;
  --ink:#1d2a2a;
  --mist:#e8efec;
  --rule:#d9cdb6;
  --page:#d9d9d9;
  --white:#ffffff;
}
*{box-sizing:border-box;margin:0;padding:0}
html,body{width:949px;height:1200px;overflow:hidden;background:var(--page)}
.flyer{
  position:absolute;left:42.7px;top:41.3px;width:1275px;height:1649px;
  transform:scale(0.6779);transform-origin:0 0;
  background:var(--white);overflow:hidden;
  font-family:"Figtree",sans-serif;color:var(--ink);
}
.abs{position:absolute}
.waves{position:absolute;left:0;top:0}
.headline{left:0;width:1275px;text-align:center;font-family:"Playfair Display",serif;color:var(--white);line-height:1}
.headline-1{top:62px;font-size:104px;font-weight:400}
.headline-2{top:164px;font-size:108px;font-weight:700}
.headline-2 .accent{color:var(--gold-text)}
.approval-badge{left:167px;top:299px;width:930px;height:64px;background:var(--white);border:2px solid var(--gold);border-radius:4px;display:flex;align-items:center}
.approval-badge .seal{width:72px;height:100%;background:var(--gold);display:flex;align-items:center;justify-content:center}
.approval-badge .label{flex:1;text-align:center;font-size:32px;color:var(--ink);white-space:nowrap}
.approval-badge b{font-weight:700}
.supporting{left:0;top:392px;width:1275px;text-align:center;color:var(--white);font-size:30px;line-height:40px;font-weight:400}
.supporting .accent{color:var(--gold-text);font-weight:600}
.section-tag{left:454px;top:641px;width:361px;height:1px;background:var(--ink)}
.section-tag span{position:absolute;left:58px;top:-20px;width:258px;height:40px;background:var(--gold);color:var(--white);font-weight:800;font-size:30px;line-height:40px;text-align:center;border-radius:3px}
.grid-line{background:var(--rule)}
.service{display:flex;align-items:center;gap:22px}
.service .ring{width:88px;height:88px;border-radius:50%;background:var(--green-deep);border:4px solid var(--gold);display:flex;align-items:center;justify-content:center;flex:none}
.service p{font-size:23px;line-height:30px;color:var(--ink);white-space:nowrap}
.trust-bar{left:77px;top:957px;width:1121px;height:132px;background:var(--mist);border-radius:14px}
.trust-title{left:22px;top:34px;font-size:23px;font-weight:800;line-height:30px;color:var(--green-deep)}
.trust-item{top:14px;text-align:center;font-size:22px;line-height:25px;color:var(--green-deep)}
.trust-item svg{display:block;margin:0 auto 6px}
.trust-divider{top:16px;width:1px;height:104px;background:var(--green-deep);opacity:.7}
.proof-ring{left:137px;top:1124px;width:90px;height:90px;border-radius:50%;background:var(--green-deep);border:4px solid var(--gold);display:flex;align-items:center;justify-content:center}
.proof-text{left:258px;top:1126px;font-size:31px;line-height:42px;color:var(--ink);white-space:nowrap}
.proof-text b{font-weight:700}
.logo-slot{left:427px;top:1309px;width:387px;height:90px;border:1.5px solid rgba(201,154,82,.55);border-radius:8px;color:var(--white)}
.logo-slot .bar{position:absolute;left:88px;top:12px;width:1px;height:66px;background:var(--white)}
.logo-slot .name{position:absolute;left:106px;top:8px;font-size:42px;font-weight:800;line-height:48px}
.logo-slot .sub{position:absolute;left:108px;top:56px;width:262px;text-align:center;font-size:20px;line-height:22px;display:flex;align-items:center;gap:8px}
.logo-slot .sub::before,.logo-slot .sub::after{content:"";flex:1;height:1px;background:var(--white)}
.cta-icon{left:76px;top:1476px;width:72px;height:72px;border-radius:50%;background:var(--gold);box-shadow:0 0 0 3px #3b5a52;display:flex;align-items:center;justify-content:center}
.cta-line{left:169px;color:var(--white);white-space:nowrap}
.cta-1{top:1438px;font-size:38px;font-weight:300;line-height:44px}
.cta-2{top:1478px;font-size:57px;font-weight:800;line-height:62px;color:#eef2f0}
.cta-3{top:1536px;font-size:40px;font-weight:800;line-height:46px;color:var(--gold-text)}
.cta-divider{left:660px;top:1449px;width:1px;height:125px;background:var(--white);opacity:.8}
.contact-label{left:724px;top:1446px;font-size:22px;color:var(--white)}
.contact-line{left:688px;color:var(--white);font-weight:700;display:flex;align-items:center;gap:12px;white-space:nowrap}
.contact-phone{top:1484px;font-size:38px;line-height:46px}
.contact-email{top:1536px;font-size:28px;line-height:36px}
.contact-line .dot{width:22px;height:22px;border-radius:50%;background:var(--gold);display:flex;align-items:center;justify-content:center;flex:none}
</style>
</head>
<body>
<main class="flyer">
  <svg class="waves" width="1275" height="1649" viewBox="0 0 1275 1649" aria-hidden="true">
    <path d="M0 0H1275V400Q640 775 0 433Z" fill="var(--gold)"/>
    <path d="M0 0H1275V390Q640 760 0 425Z" fill="var(--teal-band)"/>
    <path d="M0 0H1275V412Q640 740 0 420Z" fill="var(--green-deep)"/>
    <path d="M0 1384Q637 1064 1275 1384V1649H0Z" fill="var(--gold)"/>
    <path d="M0 1392Q637 1080 1275 1392V1649H0Z" fill="var(--teal-band)"/>
    <path d="M0 1394Q637 1110 1275 1410V1649H0Z" fill="var(--green-deep)"/>
  </svg>

  <h1 class="abs headline headline-1">The Clean Your</h1>
  <h1 class="abs headline headline-2">Residents <span class="accent">Notice.</span></h1>

  <div class="abs approval-badge">
    <div class="seal">
      <svg width="40" height="46" viewBox="0 0 40 46"><path d="M20 3L36 9V22C36 32 29 39 20 43C11 39 4 32 4 22V9Z" fill="#fff"/><path d="M13 23L18 28L28 17" stroke="var(--gold)" stroke-width="3.5" fill="none" stroke-linecap="round" stroke-linejoin="round"/></svg>
    </div>
    <p class="label"><b>Brookvale Homes's</b> Approved Austin Cleaning Company.</p>
  </div>

  <p class="abs supporting">Preferred Vendor Partner in BVH's Capital Partner Roster Circle.<br>Texas-owned, <span class="accent">serving Austin for 20+ years.</span></p>

  <div class="abs section-tag"><span>OUR SERVICES</span></div>

  <div class="abs grid-line" style="left:77px;top:818px;width:1021px;height:1px"></div>
  <div class="abs grid-line" style="left:322px;top:700px;width:1px;height:210px"></div>
  <div class="abs grid-line" style="left:622px;top:700px;width:1px;height:210px"></div>
  <div class="abs grid-line" style="left:948px;top:700px;width:1px;height:210px"></div>

  <div class="abs service" style="left:77px;top:700px">
    <div class="ring"><svg width="48" height="52" viewBox="0 0 48 52" fill="none" stroke="#fff" stroke-width="2"><path d="M12 10h14v6H12zM14 16l-2 8h14l-3-8M12 24h14v22H12zM26 12h6M16 33h6v8h-6z"/><circle cx="37" cy="8" r="1"/><circle cx="41" cy="12" r="1"/><circle cx="41" cy="4" r="1"/></svg></div>
    <p>Recurring<br>Janitorial</p>
  </div>
  <div class="abs service" style="left:344px;top:700px">
    <div class="ring"><svg width="52" height="48" viewBox="0 0 52 48" fill="none" stroke="#fff" stroke-width="2"><path d="M6 6v26h38M6 32v6h38v-6M40 6v16H28v-8h-8v14"/><circle cx="36" cy="35" r="3"/><path d="M10 42h14" stroke-dasharray="2 2"/></svg></div>
    <p>Floor Strip<br>Wax And Buff</p>
  </div>
  <div class="abs service" style="left:645px;top:700px">
    <div class="ring"><svg width="52" height="52" viewBox="0 0 52 52" fill="none" stroke="#fff" stroke-width="2"><path d="M34 4L26 28M20 30l12 4-4 10-14-4zM10 44c6 4 18 4 22 0"/><circle cx="40" cy="36" r="3"/><circle cx="44" cy="28" r="2"/><path d="M8 14l6 2M6 22l6 0M12 8l4 4"/></svg></div>
    <p>Carpet<br>Extraction</p>
  </div>
  <div class="abs service" style="left:973px;top:700px">
    <div class="ring"><svg width="50" height="50" viewBox="0 0 50 50" fill="none" stroke="#fff" stroke-width="2"><rect x="6" y="8" width="30" height="36"/><path d="M21 8v36M6 26h30M10 20l6-6M25 38l6-6"/><path d="M40 4v10M35 9h10"/></svg></div>
    <p>windows<br>and glass</p>
  </div>
  <div class="abs service" style="left:77px;top:838px">
    <div class="ring"><svg width="48" height="52" viewBox="0 0 48 52" fill="none" stroke="#fff" stroke-width="2"><path d="M12 10h14v6H12zM14 16l-2 8h14l-3-8M12 24h14v22H12zM26 12h6M16 33h6v8h-6z"/><circle cx="37" cy="8" r="1"/><circle cx="41" cy="12" r="1"/><circle cx="41" cy="4" r="1"/></svg></div>
    <p>Upholstery<br>Care</p>
  </div>
  <div class="abs service" style="left:344px;top:838px">
    <div class="ring"><svg width="52" height="48" viewBox="0 0 52 48" fill="none" stroke="#fff" stroke-width="2"><path d="M6 6v26h38M6 32v6h38v-6M40 6v16H28v-8h-8v14"/><circle cx="36" cy="35" r="3"/><path d="M10 42h14" stroke-dasharray="2 2"/></svg></div>
    <p>Pressure<br>Washing</p>
  </div>
  <div class="abs service" style="left:645px;top:838px">
    <div class="ring"><svg width="52" height="52" viewBox="0 0 52 52" fill="none" stroke="#fff" stroke-width="2"><path d="M34 4L26 28M20 30l12 4-4 10-14-4zM10 44c6 4 18 4 22 0"/><circle cx="40" cy="36" r="3"/><circle cx="44" cy="28" r="2"/><path d="M8 14l6 2M6 22l6 0M12 8l4 4"/></svg></div>
    <p>move-in &amp;<br>move-out cleans</p>
  </div>
  <div class="abs service" style="left:973px;top:838px">
    <div class="ring"><svg width="50" height="50" viewBox="0 0 50 50" fill="none" stroke="#fff" stroke-width="2"><rect x="6" y="8" width="30" height="36"/><path d="M21 8v36M6 26h30M10 20l6-6M25 38l6-6"/><path d="M40 4v10M35 9h10"/></svg></div>
    <p>damage<br>restoration</p>
  </div>

  <section class="abs trust-bar">
    <p class="abs trust-title">YOU CAN<br>COUNT ON US</p>
    <div class="abs trust-divider" style="left:217px"></div>
    <div class="abs trust-item" style="left:220px;width:160px">
      <svg width="44" height="48" viewBox="0 0 44 48" fill="none" stroke="var(--green-deep)" stroke-width="2"><path d="M22 3l17 6v13c0 11-8 19-17 23C13 41 5 33 5 22V9z"/><circle cx="22" cy="24" r="9"/><path d="M18 24l3 3 5-6"/></svg>
      licensed<br>&amp; Insured</div>
    <div class="abs trust-divider" style="left:379px"></div>
    <div class="abs trust-item" style="left:382px;width:222px">
      <svg width="66" height="48" viewBox="0 0 66 48" fill="none" stroke="var(--green-deep)" stroke-width="2"><circle cx="33" cy="12" r="8"/><circle cx="15" cy="16" r="6"/><circle cx="51" cy="16" r="6"/><path d="M19 44c0-12 6-18 14-18s14 6 14 18zM4 42c0-9 4-14 11-14M62 42c0-9-4-14-11-14"/></svg>
      Background-<br>Checked Crews</div>
    <div class="abs trust-divider" style="left:605px"></div>
    <div class="abs trust-item" style="left:608px;width:178px">
      <svg width="40" height="48" viewBox="0 0 40 48" fill="none" stroke="var(--green-deep)" stroke-width="2"><rect x="4" y="3" width="32" height="42" rx="2"/><rect x="9" y="11" width="6" height="6"/><rect x="9" y="21" width="6" height="6"/><rect x="9" y="31" width="6" height="6"/><path d="M19 14h12M19 24h12M19 34h12"/></svg>
      TrudeLink<br>Compliant</div>
    <div class="abs trust-divider" style="left:785px"></div>
    <div class="abs trust-item" style="left:790px;width:330px">
      <svg width="44" height="48" viewBox="0 0 44 48" fill="none" stroke="var(--green-deep)" stroke-width="2"><rect x="12" y="3" width="28" height="40" rx="2"/><path d="M20 12h14M26 20h8M26 28h8M20 36h14"/><circle cx="14" cy="26" r="9" fill="var(--mist)"/><path d="M10 26l3 3 5-6"/></svg>
      Invoicing Through Supplier<br>Nook And Halvex Systems</div>
  </section>

  <div class="abs proof-ring">
    <svg width="56" height="40" viewBox="0 0 56 40" fill="none" stroke="#fff" stroke-width="2.2" stroke-linejoin="round"><path d="M2 8l10-2 8 18-8 4zM54 8l-10-2-8 18 8 4zM12 26l10 9c2 2 5 1 6-1M20 12c4-3 9-4 14-1l10 12M28 12l-7 7c-1 2 1 4 3 3l6-4 8 8M24 30l4 3M28 26l5 5"/></svg>
  </div>
  <p class="abs proof-text">Already trusted by BVH communities.<br>Ask your peers at <b>The Wendlow</b> and <b>The Fennick on Garrow.</b></p>

  <div class="abs logo-slot">
    <span class="bar"></span>
    <span class="name">LOGO HERE</span>
    <span class="sub">LOGO HERE</span>
  </div>

  <div class="abs cta-icon">
    <svg width="40" height="40" viewBox="0 0 40 40"><rect x="4" y="7" width="32" height="29" rx="4" fill="#fff"/><rect x="11" y="3" width="3" height="8" rx="1.5" fill="#fff"/><rect x="26" y="3" width="3" height="8" rx="1.5" fill="#fff"/><g fill="var(--gold)"><rect x="9" y="19" width="5" height="4"/><rect x="17.5" y="19" width="5" height="4"/><rect x="26" y="19" width="5" height="4"/><rect x="9" y="27" width="5" height="4"/><rect x="17.5" y="27" width="5" height="4"/><rect x="26" y="27" width="5" height="4"/></g></svg>
  </div>
  <p class="abs cta-line cta-1">BOOK A FREE</p>
  <p class="abs cta-line cta-2">WALKTHROUGH</p>
  <p class="abs cta-line cta-3">OF YOUR COMMUNITY.</p>

  <div class="abs cta-divider"></div>
  <p class="abs contact-label">Call Or Email:</p>
  <p class="abs contact-line contact-phone"><span class="dot"><svg width="12" height="12" viewBox="0 0 12 12"><path d="M2 1l2 0 1 3-1.5 1c.6 1.4 1.6 2.4 3 3L7.5 6.5l3 1v2C10.5 10.5 9.5 11 8.5 11 4.5 10.5 1.5 7.5 1 3.5 1 2.5 1.5 1 2 1z" fill="var(--green-deep)"/></svg></span>512-555-0147</p>
  <p class="abs contact-line contact-email"><span class="dot"><svg width="12" height="10" viewBox="0 0 12 10" fill="none" stroke="var(--green-deep)" stroke-width="1.4"><rect x="1" y="1" width="10" height="8"/><path d="M1 1l5 4 5-4"/></svg></span>support@quillonclean-example.com</p>
</main>
</body>
</html>
```